Brann's Accord business card design

I am a private mediator and family dispute resolution practitioner. I am located on Gold Coast, Australia. Private mediation is mandatory within the Family Law Act so I offer very affordable private mediation for families and workplace and community. We also offer education and workshops training and development for schools, families and businesses based on becoming more open and effective communicator and anti conflict resolution, dispute resolution. We facilitate crucial conversations and help families create parenting agreements/plans about their children and situation and people to live in harmony even though they may disagree. We would like to see designs that are simple that use vibrant pink/purple, poppy red and vibrant blue (colour of communication) or yellow or vibrant lime green. We would like the design represent new growth, moving forward in separate ways but harmony similar to a seed (circle open at the top) with new shoots in opposite direction. The final design should communicate moving forward in slightly different ways with the principle from family represented by seed or something similar.

Industry/Entity Type

Business

Contact Information for Business Card

Brann's Accord, Marla Brann,PO Box 152, Robina Qld 4226Effective Private Mediation, Anti Conflict Coaching, Couples and individual coaching. family | workplace | community Competitive rates | after hour appointments. Nationally Accredited Mediator, Family Dispute Resolution Practitioner M: 0427561904 E: marlabrann3@quellmail.com

Font styles to use
Sans Serif

Colors
a64599
fbed22
ec1f27
fff5ef

Requirements
Must have
• colour and be double sided
• vibrant poppy colour red is my preference blended or contrasted with purple or other contrast colour
• elegant professional font cannot add file for some reason below under image or sketch but google images have good variety of red/orange colour of poppy flower that I like
Nice to have
• graduated colour from left to right
Should not have
• no capital/ block text that look solid or chunky

```html
<!DOCTYPE html>
<html lang="en">
<head>
<meta charset="utf-8">
<title>Brann's Accord – Business Card</title>
<link rel="stylesheet" href="https://fonts.googleapis.com/css2?family=Open+Sans:wght@400;600&display=swap">
<style>
  :root {
    --stage: #3b3532;
    --card: #0e0e0f;
    --card-edge: #1d1d20;
    --purple: #8a5cc4;
    --purple-soft: #9b6fd6;
    --white: #f4f4f4;
    --grey: #bdbdbd;
    --silver: #c4c4c4;
    --rule: #4a4a4e;
  }
  * { margin: 0; padding: 0; box-sizing: border-box; }
  html, body {
    width: 1200px; height: 844px; overflow: hidden;
    background: var(--stage);
    font-family: "Open Sans", Arial, sans-serif;
  }
  .stage {
    position: relative; width: 1200px; height: 844px;
    display: flex; align-items: center; justify-content: center; gap: 40px;
  }
  .card {
    position: relative; width: 540px; height: 320px;
    background: var(--card);
    border: 1px solid var(--card-edge);
    border-radius: 4px;
  }

  /* Front side */
  .brand {
    position: absolute; left: 0; right: 0; top: 36px;
    display: flex; flex-direction: column; align-items: center; gap: 12px;
  }
  .brand-mark {
    width: 46px; height: 46px;
    border: 3px solid var(--white);
  }
  .brand-name {
    font-weight: 400; font-size: 32px; letter-spacing: 1.5px;
    color: var(--white); line-height: 1;
  }
  .details {
    position: absolute; left: 0; right: 0; top: 178px;
    display: flex; justify-content: center;
  }
  .person {
    width: 250px; padding: 22px 18px 0 0; text-align: right;
    border-right: 1px solid var(--rule);
  }
  .person-name { color: var(--purple-soft); font-size: 21px; font-weight: 600; line-height: 1.1; }
  .person-role { color: var(--grey); font-size: 13px; margin-top: 2px; }
  .person-address { color: var(--white); font-size: 15px; line-height: 1.3; margin-top: 14px; }
  .contacts { list-style: none; padding-left: 16px; width: 250px; }
  .contacts li {
    display: flex; align-items: center; gap: 9px;
    color: var(--white); font-size: 13.5px; height: 24px;
  }
  .contact-icon {
    width: 17px; height: 17px; border-radius: 3px; flex: none;
    background: var(--purple); display: flex; align-items: center; justify-content: center;
  }
  .contact-icon svg { width: 10px; height: 10px; }

  /* Back side */
  .back-brand {
    position: absolute; inset: 0;
    display: flex; flex-direction: column; align-items: center; justify-content: center; gap: 22px;
  }
  .back-brand .brand-mark { width: 56px; height: 56px; border-color: var(--silver); }
  .back-brand .brand-name { color: var(--silver); font-size: 36px; }
</style>
</head>
<body>
<main class="stage">
  <section class="card card-front" aria-label="Card front">
    <div class="brand">
      <div class="brand-mark"></div>
      <div class="brand-name">Brann's Accord</div>
    </div>
    <div class="details">
      <div class="person">
        <div class="person-name">Marla Brann</div>
        <div class="person-role">Managing Director</div>
        <div class="person-address">PO Box 687,<br>Tarwin Qld 4391</div>
      </div>
      <ul class="contacts">
        <li><span class="contact-icon"><svg viewBox="0 0 10 10"><path d="M2 1h2l1 2-1.2 1a5 5 0 0 0 2.2 2.2L7 5l2 1v2a1 1 0 0 1-1 1A7 7 0 0 1 1 2a1 1 0 0 1 1-1z" fill="#fff"/></svg></span>0427561904</li>
        <li><span class="contact-icon"><svg viewBox="0 0 10 10"><rect x="2.5" y="0.5" width="5" height="9" rx="1" fill="none" stroke="#fff"/><circle cx="5" cy="8" r="0.6" fill="#fff"/></svg></span>0438215067</li>
        <li><span class="contact-icon"><svg viewBox="0 0 10 10"><rect x="0.5" y="2" width="9" height="6" fill="none" stroke="#fff"/><path d="M0.5 2L5 5.5 9.5 2" fill="none" stroke="#fff"/></svg></span>marlabrann3@quellmail.com</li>
        <li><span class="contact-icon"><svg viewBox="0 0 10 10"><path d="M4 6L6 4M3.5 4.5l-1.5 1.5a1.4 1.4 0 0 0 2 2l1.5-1.5M6.5 5.5L8 4a1.4 1.4 0 0 0-2-2L4.5 3.5" fill="none" stroke="#fff" stroke-linecap="round"/></svg></span>www.brannsaccord.com.au</li>
      </ul>
    </div>
  </section>

  <section class="card card-back" aria-label="Card back">
    <div class="back-brand">
      <div class="brand-mark"></div>
      <div class="brand-name">Brann's Accord</div>
    </div>
  </section>
</main>
</body>
</html>
```